Kelmora Lodges internet banner add

Seldovia Alaska -I need a fabulous UNIQUE web banner for our two locations Kelmora Lodges Harbor Location and Kelmora Lodges Central location
All suites have full Kitchens
Open year Round
We cater to vacationers - fishermen - hikers - and families
Classy upbeat modern design
The dimensions for the banner ads are:

300x250
OR
728x90

Target Market(s)

Alaska- Nautical

Industry/Entity Type

Vacation rentals

Requirements
Must have
• I would like the attached photo as background Kelmora Lodges - every path brings you home with our phone number- email - and 2 websites

```html
<!DOCTYPE html>
<html lang="en">
<head>
<meta charset="utf-8">
<title>Kelmora Lodges – Web Banners</title>
<link rel="stylesheet" href="https://fonts.googleapis.com/css2?family=Arimo:wght@400;700&display=swap">
<style>
  :root {
    --stage: #e8e8e8;
    --red: #d12027;
    --yellow: #fad51c;
    --black: #050505;
    --white: #ffffff;
    --ink: #111111;
    --sky-top: #a9c4dc;
    --forest: #3d4f35;
    --shore: #6f6a5e;
    --interior-a: #5a3a22;
    --interior-b: #b38a52;
    --interior-c: #2f8f8f;
  }
  * { box-sizing: border-box; margin: 0; padding: 0; }
  html, body {
    width: 1200px; height: 562px; overflow: hidden;
    background: var(--stage);
    font-family: "Arimo", Arial, sans-serif;
  }
  .stage { position: relative; width: 1200px; height: 562px; }
  .banner {
    position: absolute; top: 62px;
    width: 522px; height: 435px;
    display: grid; grid-template-columns: 261px 261px;
    box-shadow: 0 6px 14px rgba(0,0,0,.18);
  }
  .banner--central { left: 62px; }
  .banner--harbor { left: 633px; }

  .visual-column { display: grid; grid-template-rows: 126px 133px 86px 90px; }
  .photo-exterior {
    background: linear-gradient(180deg, var(--sky-top) 0%, #c9d8e2 28%, var(--forest) 45%, #56624a 70%, var(--shore) 100%);
  }
  .photo-interior {
    background: linear-gradient(90deg, var(--interior-a) 0%, #7a5535 38%, var(--interior-b) 60%, #c9a86a 78%, var(--interior-c) 100%);
  }
  .location-plate {
    background: var(--yellow); color: var(--ink);
    display: flex; flex-direction: column; align-items: center; justify-content: center;
    text-align: center;
  }
  .location-name { font-weight: 700; font-size: 19px; line-height: 23px; letter-spacing: .2px; }
  .location-tagline { font-weight: 700; font-size: 8.5px; margin-top: 7px; letter-spacing: -.1px; }
  .brand-block {
    background: var(--black);
    display: flex; align-items: center; justify-content: center; gap: 9px;
  }
  .brand-mark { width: 12px; height: 12px; background: var(--white); }
  .brand-name { color: var(--white); font-weight: 700; font-size: 21px; letter-spacing: 1.5px; }

  .message-column {
    background: var(--red); position: relative;
    padding: 28px 0 0 26px;
  }
  .headline { color: var(--white); font-weight: 700; font-size: 23.5px; line-height: 31px; }
  .season { color: var(--yellow); font-weight: 700; font-size: 20px; margin-top: 20px; }
  .audience { list-style: none; margin-top: 14px; }
  .audience li {
    color: var(--yellow); font-size: 15.5px; line-height: 22.5px;
    display: flex; align-items: center; gap: 8px;
  }
  .audience svg { width: 14px; height: 12px; flex: none; }
  .style-note {
    color: var(--yellow); font-weight: 700; font-size: 23.5px; line-height: 31px;
    margin-top: 26px;
  }
  .cta {
    position: absolute; left: 27px; top: 369px;
    width: 200px; height: 42px;
    background: var(--yellow); color: var(--ink);
    display: flex; align-items: center; justify-content: center;
    font-weight: 700; font-size: 14px; letter-spacing: .6px; text-decoration: none;
  }
</style>
</head>
<body>
<main class="stage">

  <section class="banner banner--central">
    <div class="visual-column">
      <div class="photo-exterior" role="img" aria-label="Waterfront lodge building above a rocky shoreline with evergreen forest"></div>
      <div class="photo-interior" role="img" aria-label="Suite interior with wooden door, sofa and window view"></div>
      <div class="location-plate">
        <p class="location-name">KELMORA LODGES<br>CENTRAL LOCATION</p>
        <p class="location-tagline">FULLY-FURNISHED WATERFRONT APARTMENT</p>
      </div>
      <div class="brand-block">
        <span class="brand-mark"></span><span class="brand-name">KELMORA LODGES</span>
      </div>
    </div>
    <div class="message-column">
      <h2 class="headline">ALL SUITES HAVE<br>FULL KITCHENS</h2>
      <p class="season">OPEN YEAR ROUND</p>
      <ul class="audience">
        <li><svg viewBox="0 0 14 12"><path d="M1 6.5 5 10 13 1.5" fill="none" stroke="#fad51c" stroke-width="2.6"/></svg>We cater to vacationers</li>
        <li><svg viewBox="0 0 14 12"><path d="M1 6.5 5 10 13 1.5" fill="none" stroke="#fad51c" stroke-width="2.6"/></svg>Fishermen</li>
        <li><svg viewBox="0 0 14 12"><path d="M1 6.5 5 10 13 1.5" fill="none" stroke="#fad51c" stroke-width="2.6"/></svg>Hikers</li>
        <li><svg viewBox="0 0 14 12"><path d="M1 6.5 5 10 13 1.5" fill="none" stroke="#fad51c" stroke-width="2.6"/></svg>and families</li>
      </ul>
      <p class="style-note">CLASSY UPBEAT<br>MODERN DESIGN</p>
      <a class="cta" href="#">LEARN MORE</a>
    </div>
  </section>

  <section class="banner banner--harbor">
    <div class="visual-column">
      <div class="photo-exterior" role="img" aria-label="Waterfront lodge building above a rocky shoreline with evergreen forest"></div>
      <div class="photo-interior" role="img" aria-label="Suite interior with wooden door, sofa and window view"></div>
      <div class="location-plate">
        <p class="location-name">KELMORA LODGES<br>HARBOR LOCATION</p>
        <p class="location-tagline">FULLY-FURNISHED WATERFRONT APARTMENT</p>
      </div>
      <div class="brand-block">
        <span class="brand-mark"></span><span class="brand-name">KELMORA LODGES</span>
      </div>
    </div>
    <div class="message-column">
      <h2 class="headline">ALL SUITES HAVE<br>FULL KITCHENS</h2>
      <p class="season">OPEN YEAR ROUND</p>
      <ul class="audience">
        <li><svg viewBox="0 0 14 12"><path d="M1 6.5 5 10 13 1.5" fill="none" stroke="#fad51c" stroke-width="2.6"/></svg>We cater to vacationers</li>
        <li><svg viewBox="0 0 14 12"><path d="M1 6.5 5 10 13 1.5" fill="none" stroke="#fad51c" stroke-width="2.6"/></svg>Fishermen</li>
        <li><svg viewBox="0 0 14 12"><path d="M1 6.5 5 10 13 1.5" fill="none" stroke="#fad51c" stroke-width="2.6"/></svg>Hikers</li>
        <li><svg viewBox="0 0 14 12"><path d="M1 6.5 5 10 13 1.5" fill="none" stroke="#fad51c" stroke-width="2.6"/></svg>and families</li>
      </ul>
      <p class="style-note">CLASSY UPBEAT<br>MODERN DESIGN</p>
      <a class="cta" href="#">LEARN MORE</a>
    </div>
  </section>

</main>
</body>
</html>
```